LumaWireHub full website re-design

I'm looking for a current, cool new design of my website, lumawirehub-example.com. We sell fiber optic cables and accessories. It hasn't been changed for over 10 years. I would like fresh ideas, not excessive pictures of cables. It has to be easy to navigate because we have over 5k products that we sell. The platform that our site is built on is Prestashop. I've attached many of our popular brands as well as some of our products so you can get an idea of what we sell. I also encourage you to go to our current website to see everything we offer. We are a high end brand and I want to give that impression. The winning designer will likely have ongoing work in the future because we will be making changes and additions to our site. Prestashop experience preferred! Be creative as you want. I would like banner images across the top as well.

Target Market(s)

Men 20-50

Industry/Entity Type

Technology

Coding

Coded - Design and coding required

Number of Pages Required

5+ page

Requirements
Must have
• https://www.videohost-example.com/watch?v=Qm7TzRb2pXo
Should not have
• cartoons

```html
<!DOCTYPE html>
<html lang="en">
<head>
<meta charset="utf-8">
<title>LumaWireHub – Website Redesign Pages</title>
<link href="https://fonts.googleapis.com/css2?family=Roboto:wght@300;400;500;700;900&display=swap" rel="stylesheet">
<style>
:root{
  --crimson:#9b1740;
  --crimson-dark:#7c1032;
  --board:#606060;
  --ink:#1d1d1d;
  --muted:#6a6a6a;
  --line:#dedede;
  --soft:#f3f3f3;
  --black:#000;
  --white:#fff;
  --green:#1faa3c;
}
*{box-sizing:border-box;margin:0;padding:0}
html,body{width:767px;height:1200px;overflow:hidden;background:var(--board)}
body{font-family:'Roboto',sans-serif;color:var(--ink)}
.board{position:relative;width:767px;height:1200px;background:var(--board);overflow:hidden}
.board-label{position:absolute;color:var(--white);font:500 12.5px 'Roboto',sans-serif;transform:translateX(-50%);white-space:nowrap}

.page{position:absolute;width:200px;background:var(--white);overflow:hidden}
.topbar{height:6px;background:#ececec;display:flex;justify-content:space-between;align-items:center;padding:0 12px;font-size:2.4px;color:#333}
.topbar b{color:var(--crimson)}
.topbar span+span{margin-left:5px}
.masthead{height:17px;display:flex;align-items:center;padding:0 12px;gap:7px}
.wordmark{display:flex;align-items:center;gap:2px;font:700 5.6px 'Roboto',sans-serif;color:var(--crimson);width:50px}
.wordmark i{width:4px;height:4px;border-radius:50%;background:var(--crimson);display:block}
.search{flex:1;height:6px;border:.4px solid #ccc;border-radius:3px;display:flex;align-items:center;justify-content:space-between;font-size:2.2px;color:#999;padding-left:3px;overflow:hidden}
.search b{height:100%;width:21px;background:var(--crimson);color:var(--white);border-radius:3px;display:flex;align-items:center;justify-content:center;font-size:2.3px}
.utils{display:flex;gap:3px;align-items:center}
.utils svg{width:5px;height:5px}
.nav{height:13px;background:var(--crimson);display:flex;align-items:center;padding-left:12px;font:700 2.3px 'Roboto',sans-serif;color:var(--white)}
.nav span{padding:0 4.5px}
.nav .cats{background:rgba(255,255,255,.18);height:100%;display:flex;align-items:center;padding:0 6px}
.hero{position:relative;height:58px;background:linear-gradient(100deg,#1c1a27 0%,#3f2236 35%,#28344e 62%,#45172f 100%)}
.hero h1{position:absolute;left:0;right:0;top:18px;text-align:center;color:var(--white);font:700 10.5px 'Roboto',sans-serif;letter-spacing:.1px}
.hero svg{position:absolute;left:0;bottom:0;width:200px;height:14px}
.body{position:absolute;left:0;right:0;top:94px}
.abs{position:absolute}

.section-title{position:absolute;left:0;right:0;text-align:center;font:700 6.3px 'Roboto',sans-serif;color:#555}
.section-title em{font-style:normal;color:var(--crimson)}
.copy{font-size:2.2px;line-height:1.45;color:#444;text-align:center}
.copy-left{font-size:2.1px;line-height:1.45;color:#444;text-align:justify}
.copy a{color:var(--crimson);font-weight:700;text-decoration:underline}

.brands{position:absolute;left:23px;width:153px;height:31px;border-radius:4px;background:var(--white);box-shadow:0 0 3px rgba(0,0,0,.15);display:flex;justify-content:space-around;align-items:center;font:700 4.6px 'Roboto',sans-serif;color:#333}

.form-card{position:absolute;left:33px;width:134px;height:103px;background:var(--white);border-radius:4px;box-shadow:0 0 4px rgba(0,0,0,.14);padding:9px 8px}
.form-grid{display:grid;grid-template-columns:1fr 1fr;column-gap:5px}
.form-card h4{font:400 3.6px 'Roboto',sans-serif;color:#777;margin-bottom:4px}
.field{height:8px;border:.4px solid #ddd;font-size:1.8px;color:#aaa;padding:2.5px 2px;margin-bottom:4.5px;position:relative}
.field.select::after{content:"▾";position:absolute;right:2px;top:2.3px}
.field.msg{height:46px}
.btn{display:flex;align-items:center;justify-content:center;color:var(--white);background:var(--crimson);font:700 2.6px 'Roboto',sans-serif;border-radius:5px}
.form-card .btn{width:30px;height:9px;margin:3px auto 0}

.grid{position:absolute;left:19px;top:30px;display:grid;grid-template-columns:repeat(4,37px);grid-auto-rows:62px;column-gap:5px;row-gap:8px}
.card{border-radius:3px;background:var(--white);box-shadow:0 0 2.5px rgba(0,0,0,.2);text-align:center;padding-top:2px;overflow:hidden}
.card.is-hover{border:.6px solid var(--crimson)}
.card .thumb{height:27px;margin:0 3px;background:linear-gradient(160deg,#f5f3ef,#d8d2c4 60%,#e9e6df)}
.card b{display:block;color:var(--crimson);font:700 3.6px 'Roboto',sans-serif;margin-top:7px}
.card p{font-size:1.9px;color:#777;line-height:1.3;margin:2px 5px 0}
.acts{display:flex;justify-content:center;gap:1.5px;margin-top:3px}
.acts i{width:5px;height:5px;border-radius:50%;border:.4px solid #bbb;display:block}
.acts i.cart{border-color:var(--crimson)}

.footer{position:absolute;left:0;right:0;bottom:0;height:81px;background:var(--black);color:var(--white)}
.footer h3{position:absolute;top:7px;left:0;right:0;text-align:center;font:500 6px 'Roboto',sans-serif}
.news{position:absolute;top:19px;left:46px;display:flex;gap:1px}
.news span{width:86px;height:6px;border:.4px solid #555;border-radius:3px;font-size:1.9px;color:#888;padding:1.6px 3px}
.news b{width:17px;height:6px;border-radius:3px;background:var(--crimson);font-size:2.3px;display:flex;align-items:center;justify-content:center}
.contact{position:absolute;top:37px;display:flex;align-items:center;gap:2px;font-size:2px;line-height:1.3}
.contact .ring{width:10px;height:10px;border:.6px solid var(--white);border-radius:50%;display:flex;align-items:center;justify-content:center;flex:none}
.contact .ring svg{width:5px;height:5px}
.contact strong{font-size:2.3px;display:block}
.contact .big{font-size:3px;font-weight:500}
.socials{position:absolute;top:65px;left:21px;display:flex;gap:1.5px}
.socials i{width:5px;height:5px;border:.4px solid var(--white);border-radius:50%;display:block}
.foot-mark{position:absolute;top:64px;left:72px;font:700 5.6px 'Roboto',sans-serif;color:var(--crimson);display:flex;align-items:center;gap:2px}
.foot-mark i{width:4px;height:4px;border-radius:50%;background:var(--crimson);display:block}
.copyright{position:absolute;top:65px;left:129px;font-size:1.9px;color:#ccc;line-height:1.4}

.overlay{position:absolute;left:0;right:0;top:36px;bottom:0;background:rgba(0,0,0,.58)}
.dropdown{position:absolute;left:7px;top:44px;width:186px;height:90px;background:var(--white);box-shadow:0 1px 4px rgba(0,0,0,.3);display:grid;grid-template-columns:repeat(3,1fr);padding:9px 0 0 15px}
.dropdown ul{list-style:none}
.dropdown li{font-size:2.4px;color:#444;height:9.4px}
.dropdown li::before{content:"+";color:var(--crimson);font-weight:700;margin-right:2px}

.crumbs{position:absolute;left:0;right:0;top:0;height:12px;background:#f1f1f1;font-size:2px;color:#888;padding:4px 0 0 29px}
.crumbs b{color:#333;font-weight:500}
.prod-shot{position:absolute;left:24px;top:27px;width:73px;height:73px;border-radius:4px;box-shadow:0 0 3px rgba(0,0,0,.18);background:linear-gradient(135deg,#fafafa 0%,#e8eef5 45%,#3e73b8 62%,#f0f0f0 80%)}
.thumbs{position:absolute;left:24px;top:107px;display:flex;gap:3px}
.thumbs div{width:16px;height:16px;border-radius:2px;box-shadow:0 0 2px rgba(0,0,0,.2);background:linear-gradient(135deg,#fff,#dfe6ee 50%,#6d93c6)}
.info{position:absolute;left:105px;top:27px;width:72px}
.info h2{font:500 4.6px 'Roboto',sans-serif;line-height:1.2;color:#222}
.stars{font-size:3px;color:#f2b01e;margin-top:2px}
.stars small{font-size:1.8px;color:#999}
.price{font:700 6.8px 'Roboto',sans-serif;color:var(--crimson);margin-top:2px}
.info p{font-size:1.9px;color:#666;line-height:1.45;margin-top:2px}
.opts{position:absolute;left:105px;top:104px;display:flex;gap:4px;font-size:1.9px;color:#666}
.opts .box{margin-top:1.5px;height:5.5px;border:.4px solid #ccc;display:flex;align-items:center;font-size:2px}
.qty span{width:6px;text-align:center;border-right:.4px solid #ccc}
.qty span:last-child{border:none}
.len{width:18px;padding-left:1.5px}
.paycard{margin-top:2px;width:22px;height:7px;border-radius:1.5px;border:.4px solid #ccc;font:700 2.3px 'Roboto',sans-serif;color:#333;display:flex;align-items:center;justify-content:center}
.share{position:absolute;left:105px;top:129px;display:flex;gap:1.5px}
.share span{font-size:1.7px;color:#555;border:.3px solid #ccc;border-radius:1px;padding:.5px 1.5px}
.buy{position:absolute;left:105px;top:138px;display:flex;gap:3px}
.buy .btn{height:8px;border-radius:4px;font-size:2.5px}
.buy .stock{width:23px;background:var(--green)}
.buy .add{width:27px}
.tabs-card{position:absolute;left:24px;top:167px;width:152px;height:243px;border-radius:4px;box-shadow:0 0 3px rgba(0,0,0,.18);overflow:hidden}
.tabs{height:12px;background:var(--crimson);display:flex;align-items:center;font:500 2.4px 'Roboto',sans-serif;color:var(--white)}
.tabs span{padding:0 4px}
.tabs .on{background:#3a3a3a;height:100%;display:flex;align-items:center;padding:0 9px}
.specs{padding:6px 5px 0;list-style:none}
.specs li{font-size:2.3px;line-height:1.35;color:#444;margin-bottom:2.9px}
.specs b{color:var(--crimson);font-weight:700;margin-right:2px}
.cleaners{position:absolute;left:0;right:0;top:424px;height:80px;background:#efefef}
.cleaners h3{position:absolute;top:13px;left:0;right:0;text-align:center;font:700 4.6px 'Roboto',sans-serif;color:#444}
.cleaners h3 em{font-style:normal;color:var(--crimson)}
.carousel{position:absolute;top:24px;left:24px;display:flex;gap:2px}
.carousel div{width:37px;height:36px;background:var(--white);text-align:center;font-size:2.1px;color:#555;padding-top:2px}
.carousel div span{display:block;height:22px;margin:0 4px 3px;background:linear-gradient(160deg,#fafafa,#e2dcd6 50%,#c9a28e)}
.chev{position:absolute;top:37px;font-size:9px;color:#bbb;font-weight:300}
.about-visual{position:absolute;left:24px;top:13px;width:67px;height:63px;border-radius:3px;background:linear-gradient(135deg,#f4eef1 0%,#d9c4cc 55%,#b896a4 100%)}
</style>
</head>
<body>
<svg width="0" height="0" style="position:absolute">
  <defs>
    <symbol id="i-phone" viewBox="0 0 24 24"><path d="M6.6 10.8a15 15 0 0 0 6.6 6.6l2.2-2.2c.3-.3.7-.4 1-.2 1.1.4 2.3.6 3.6.6.6 0 1 .4 1 1V20c0 .6-.4 1-1 1A17 17 0 0 1 3 4c0-.6.4-1 1-1h3.5c.6 0 1 .4 1 1 0 1.3.2 2.5.6 3.6.1.3 0 .7-.2 1z" fill="#fff"/></symbol>
    <symbol id="i-mail" viewBox="0 0 24 24"><rect x="3" y="6" width="18" height="12" rx="1.5" fill="none" stroke="#fff" stroke-width="2"/><path d="M3.5 7l8.5 6 8.5-6" fill="none" stroke="#fff" stroke-width="2"/></symbol>
    <symbol id="i-pin" viewBox="0 0 24 24"><path d="M12 2a7 7 0 0 0-7 7c0 5 7 13 7 13s7-8 7-13a7 7 0 0 0-7-7zm0 9.5A2.5 2.5 0 1 1 12 6.5a2.5 2.5 0 0 1 0 5z" fill="#fff"/></symbol>
    <symbol id="i-cart" viewBox="0 0 24 24"><path d="M3 4h3l2.5 11h10l2-8H7.5" fill="none" stroke="#555" stroke-width="2.4"/><circle cx="9.5" cy="19.5" r="1.6" fill="#555"/><circle cx="17" cy="19.5" r="1.6" fill="#555"/></symbol>
    <symbol id="i-heart" viewBox="0 0 24 24"><path d="M12 21s-8-5.3-8-11a4.5 4.5 0 0 1 8-2.8A4.5 4.5 0 0 1 20 10c0 5.7-8 11-8 11z" fill="#555"/></symbol>
    <symbol id="i-hero" viewBox="0 0 200 14" preserveAspectRatio="none"><polygon points="0,4 200,0 200,7 0,14" fill="#9b1740"/><polygon points="0,14 200,7 200,14" fill="#fff"/></symbol>
  </defs>
</svg>

<main class="board">
  <div class="board-label" style="left:130px;top:27px">About us</div>
  <div class="board-label" style="left:370px;top:11px">Products Page</div>
  <div class="board-label" style="left:593px;top:11px">Reseller Page</div>
  <div class="board-label" style="left:585px;top:454px">Single product Page</div>
  <div class="board-label" style="left:127px;top:545px">Buyers Page</div>
  <div class="board-label" style="left:356px;top:590px">Menu Dropdown Page</div>

  <!-- ABOUT -->
  <section class="page" style="left:31px;top:57px;height:469px">
    <div class="topbar"><div><b>&#9990; Call Us:</b> (555) 014-2287</div><div><span>Login</span><span>Register</span></div></div>
    <header class="masthead"><div class="wordmark"><i></i>LumaWireHub</div><div class="search">Enter Product name<b>SEARCH</b></div><div class="utils"><svg><use href="#i-cart"/></svg><svg><use href="#i-heart"/></svg></div></header>
    <nav class="nav"><span class="cats">CATEGORIES ▾</span><span>HOME</span><span>ABOUT US</span><span>LINE CARD</span><span>GOV/EDU BUYERS</span><span>RESELLERS</span><span>CONTACT</span></nav>
    <div class="hero" role="img" aria-label="Banner photo of a fiber optic patch panel"><h1>ABOUT US</h1><svg><use href="#i-hero"/></svg></div>
    <div class="body">
      <div class="about-visual" role="img" aria-label="Photo of a coiled red fiber optic patch cable"></div>
      <h2 class="abs" style="left:97px;top:13px;width:90px;font:700 6.3px 'Roboto',sans-serif;line-height:1.25;color:#555"><span style="color:var(--crimson)">WHAT IS THE LUMAWIRE</span><br>HUB EDGE?</h2>
      <p class="abs copy-left" style="left:97px;top:34px;width:76px">We want to give every one of our customers a positive experience when they do business with us. Our team of industry professionals has a combined 20 years of experience in all areas of the cable and connectivity business. The company was created to give customers a convenient place to shop online for products to meet their connectivity needs. Due to our extensive inventory we can ship many products on a same day/next day basis. We also have quick turn around time on cable assemblies and have compliant products that are made in the U.S.A. We purchase raw material directly from the fiber cable manufacturer so you save on distribution cost and our prices are extremely competitive. There is no middle man between you and LumaWireHub.</p>
      <p class="abs copy-left" style="left:29px;top:91px;width:143px">We focus on three main areas, which we believe are the most important to the customer. First of all, nobody wants to wait for cables, which is why we stock over one million cables from 1/2 meter to 300 meters in varieties such as indoor, indoor/outdoor and armored cables. We are on the west coast so we have three extra hours to ship for our east coast customers. This is why most of our orders ship in 1-2 days. Secondly, we are sticklers about quality. We use premium fiber, ceramic connectors and each cable comes individually bagged with individual test results. Because of the high quality of our cables, we are able to guarantee them for life. After all, if we can't stand behind our product, we can't expect you to. Finally, we are all familiar with the element of surprise that comes with the shipping cost of an online order. We hate shipping costs too so we got rid of them. All online orders are eligible for free ground shipping.<br><br>We really hope your experience with us is a positive one and we truly want to retain you as a customer for life. We are big enough to get things done yet small enough to care!</p>
      <div class="abs" role="img" aria-label="Company introduction video" style="left:29px;top:149px;width:143px;height:81px;background:linear-gradient(120deg,#2b2b2b,#4a4a4a 45%,#1a1a1a)">
        <svg style="position:absolute;left:64px;top:33px" width="14" height="14" viewBox="0 0 14 14"><circle cx="7" cy="7" r="6" fill="none" stroke="#fff" stroke-width=".8"/><polygon points="5.5,4.3 10,7 5.5,9.7" fill="#fff"/></svg>
        <div style="position:absolute;left:0;right:0;bottom:0;height:4px;background:rgba(0,0,0,.6);font-size:1.6px;color:#ddd;padding:1px 2px">▶ 0:10 / 0:59</div>
      </div>
      <div class="brands" style="top:252px"><span>BendRight</span><span>ShieldCore</span><span>PlayMaker</span><span>SnugPort</span></div>
    </div>
    <footer class="footer">
      <h3>Sign up for Our Newsletter</h3>
      <div class="news"><span>Email</span><b>SIGN UP</b></div>
      <div class="contact" style="left:20px"><div class="ring"><svg><use href="#i-phone"/></svg></div><div><strong>CALL US TODAY:</strong><span class="big">(555) 014-2287</span></div></div>
      <div class="contact" style="left:68px"><div class="ring"><svg><use href="#i-mail"/></svg></div><div><strong>EMAIL:</strong>sales@lumawirehub-example.com</div></div>
      <div class="contact" style="left:122px"><div class="ring"><svg><use href="#i-pin"/></svg></div><div><strong>LOCATION:</strong>Sales Office | Warehouse,<br>240 Relay Park Ave. Suite B, Fairvale,<br>CA 90000-0123<br>Hours: 8:00am - 5:00pm / Mon-Fri</div></div>
      <div class="socials"><i></i><i></i><i></i><i></i></div>
      <div class="foot-mark"><i></i>LumaWireHub</div>
      <div class="copyright">Copyright © 2021 - LumaWire Hub, Inc.<br>All Right Reserved</div>
    </footer>
  </section>

  <!-- PRODUCTS -->
  <section class="page" style="left:261px;top:40px;height:540px">
    <div class="topbar"><div><b>&#9990; Call Us:</b> (555) 014-2287</div><div><span>Login</span><span>Register</span></div></div>
    <header class="masthead"><div class="wordmark"><i></i>LumaWireHub</div><div class="search">Enter Product name<b>SEARCH</b></div><div class="utils"><svg><use href="#i-cart"/></svg><svg><use href="#i-heart"/></svg></div></header>
    <nav class="nav"><span class="cats">CATEGORIES ▾</span><span>HOME</span><span>ABOUT US</span><span>LINE CARD</span><span>GOV/EDU BUYERS</span><span>RESELLERS</span><span>CONTACT</span></nav>
    <div class="hero" role="img" aria-label="Banner photo of a fiber optic patch panel"><h1>CATEGORIES</h1><svg><use href="#i-hero"/></svg></div>
    <div class="body">
      <h2 class="section-title" style="top:10px;color:var(--crimson)">OUR PRODUCTS</h2>
      <div class="grid">
        <div class="card"><div class="thumb" role="img" aria-label="Patch cable connectors"></div><b>$8.95</b><p>OM2 LC LC Plenum Duplex Fiber Patch Cable...</p><div class="acts"><i class="cart"></i><i></i></div></div>
        <div class="card is-hover"><div class="thumb" role="img" aria-label="Patch cable connectors"></div><b>$8.95</b><p>OM2 LC LC Plenum Duplex Fiber Patch Cable...</p><div class="acts"><i class="cart"></i><i class="cart"></i></div></div>
        <div class="card"><div class="thumb" role="img" aria-label="Patch cable connectors"></div><b>$8.95</b><p>OM2 LC LC Plenum Duplex Fiber Patch Cable...</p><div class="acts"><i class="cart"></i><i></i></div></div>
        <div class="card"><div class="thumb" role="img" aria-label="Patch cable connectors"></div><b>$8.95</b><p>OM2 LC LC Plenum Duplex Fiber Patch Cable...</p><div class="acts"><i class="cart"></i><i></i></div></div>
        <div class="card"><div class="thumb" role="img" aria-label="Patch cable connectors"></div><b>$8.95</b><p>OM2 LC LC Plenum Duplex Fiber Patch Cable...</p><div class="acts"><i class="cart"></i><i></i></div></div>
        <div class="card"><div class="thumb" role="img" aria-label="Patch cable connectors"></div><b>$8.95</b><p>OM2 LC LC Plenum Duplex Fiber Patch Cable...</p><div class="acts"><i class="cart"></i><i></i></div></div>
        <div class="card"><div class="thumb" role="img" aria-label="Patch cable connectors"></div><b>$8.95</b><p>OM2 LC LC Plenum Duplex Fiber Patch Cable...</p><div class="acts"><i class="cart"></i><i></i></div></div>
        <div class="card"><div class="thumb" role="img" aria-label="Patch cable connectors"></div><b>$8.95</b><p>OM2 LC LC Plenum Duplex Fiber Patch Cable...</p><div class="acts"><i class="cart"></i><i></i></div></div>
        <div class="card"><div class="thumb" role="img" aria-label="Patch cable connectors"></div><b>$8.95</b><p>OM2 LC LC Plenum Duplex Fiber Patch Cable...</p><div class="acts"><i class="cart"></i><i></i></div></div>
        <div class="card"><div class="thumb" role="img" aria-label="Coiled aqua patch cable"></div><b>$8.95</b><p>OM2 LC LC Plenum Duplex Fiber Patch Cable...</p><div class="acts"><i class="cart"></i><i></i></div></div>
        <div class="card"><div class="thumb" role="img" aria-label="Patch cable connectors"></div><b>$8.95</b><p>OM2 LC LC Plenum Duplex Fiber Patch Cable...</p><div class="acts"><i class="cart"></i><i></i></div></div>
        <div class="card"><div class="thumb" role="img" aria-label="Fiber cleaner box"></div><b>$8.95</b><p>OM2 LC LC Plenum Duplex Fiber Patch Cable...</p><div class="acts"><i class="cart"></i><i></i></div></div>
        <div class="card"><div class="thumb" role="img" aria-label="Patch cable connectors"></div><b>$8.95</b><p>OM2 LC LC Plenum Duplex Fiber Patch Cable...</p><div class="acts"><i class="cart"></i><i></i></div></div>
        <div class="card"><div class="thumb" role="img" aria-label="Fiber cleaner pen"></div><b>$8.95</b><p>OM2 LC LC Plenum Duplex Fiber Patch Cable...</p><div class="acts"><i class="cart"></i><i></i></div></div>
        <div class="card"><div class="thumb" role="img" aria-label="Fiber cleaner box"></div><b>$8.95</b><p>OM2 LC LC Plenum Duplex Fiber Patch Cable...</p><div class="acts"><i class="cart"></i><i></i></div></div>
        <div class="card"><div class="thumb" role="img" aria-label="Patch cable connectors"></div><b>$8.95</b><p>OM2 LC LC Plenum Duplex Fiber Patch Cable...</p><div class="acts"><i class="cart"></i><i></i></div></div>
      </div>
      <div class="brands" style="top:319px"><span>BendRight</span><span>ShieldCore</span><span>PlayMaker</span><span>SnugPort</span></div>
    </div>
    <footer class="footer">
      <h3>Sign up for Our Newsletter</h3>
      <div class="news"><span>Email</span><b>SIGN UP</b></div>
      <div class="contact" style="left:20px"><div class="ring"><svg><use href="#i-phone"/></svg></div><div><strong>CALL US TODAY:</strong><span class="big">(555) 014-2287</span></div></div>
      <div class="contact" style="left:68px"><div class="ring"><svg><use href="#i-mail"/></svg></div><div><strong>EMAIL:</strong>sales@lumawirehub-example.com</div></div>
      <div class="contact" style="left:122px"><div class="ring"><svg><use href="#i-pin"/></svg></div><div><strong>LOCATION:</strong>Sales Office | Warehouse,<br>240 Relay Park Ave. Suite B, Fairvale,<br>CA 90000-0123<br>Hours: 8:00am - 5:00pm / Mon-Fri</div></div>
      <div class="socials"><i></i><i></i><i></i><i></i></div>
      <div class="foot-mark"><i></i>LumaWireHub</div>
      <div class="copyright">Copyright © 2021 - LumaWire Hub, Inc.<br>All Right Reserved</div>
    </footer>
  </section>

  <!-- RESELLER -->
  <section class="page" style="left:490px;top:40px;height:392px">
    <div class="topbar"><div><b>&#9990; Call Us:</b> (555) 014-2287</div><div><span>Login</span><span>Register</span></div></div>
    <header class="masthead"><div class="wordmark"><i></i>LumaWireHub</div><div class="search">Enter Product name<b>SEARCH</b></div><div class="utils"><svg><use href="#i-cart"/></svg><svg><use href="#i-heart"/></svg></div></header>
    <nav class="nav"><span class="cats">CATEGORIES ▾</span><span>HOME</span><span>ABOUT US</span><span>LINE CARD</span><span>GOV/EDU BUYERS</span><span>RESELLERS</span><span>CONTACT</span></nav>
    <div class="hero" role="img" aria-label="Banner photo of a fiber optic patch panel"><h1>RESELLERS</h1><svg><use href="#i-hero"/></svg></div>
    <div class="body">
      <h2 class="section-title" style="top:17px">RESELLER <em>PARTNER'S PROGRAM</em></h2>
      <p class="abs copy" style="left:34px;top:27px;width:132px">To apply for our RPP, simply fill out the form below and complete the RESALE CERTIFICATE and we will submit it to our Partners Program Department, who will process it for approval. You can also fax it to (555) 017-3390. Once approved, you will be sent a unique code which you can use to order our products. The code will automatically deduct your RPP savings. There is no obligation to buy. Once you are approved and set up, you can use your pin code anytime you purchase from LumaWireHub.</p>
      <div class="form-card" style="top:53px">
        <div class="form-grid">
          <div><h4>Subject Heading</h4><div class="field select">Choose</div><div class="field">Name</div><div class="field">Company</div><div class="field">Phone</div><div class="field">Email address</div></div>
          <div><h4>Preferred contact method</h4><div class="field select">Choose</div><div class="field msg">Message</div></div>
        </div>
        <div class="btn">SUBMIT</div>
      </div>
      <div class="brands" style="top:174px"><span>BendRight</span><span>ShieldCore</span><span>PlayMaker</span><span>SnugPort</span></div>
    </div>
    <footer class="footer">
      <h3>Sign up for Our Newsletter</h3>
      <div class="news"><span>Email</span><b>SIGN UP</b></div>
      <div class="contact" style="left:20px"><div class="ring"><svg><use href="#i-phone"/></svg></div><div><strong>CALL US TODAY:</strong><span class="big">(555) 014-2287</span></div></div>
      <div class="contact" style="left:68px"><div class="ring"><svg><use href="#i-mail"/></svg></div><div><strong>EMAIL:</strong>sales@lumawirehub-example.com</div></div>
      <div class="contact" style="left:122px"><div class="ring"><svg><use href="#i-pin"/></svg></div><div><strong>LOCATION:</strong>Sales Office | Warehouse,<br>240 Relay Park Ave. Suite B, Fairvale,<br>CA 90000-0123<br>Hours: 8:00am - 5:00pm / Mon-Fri</div></div>
      <div class="socials"><i></i><i></i><i></i><i></i></div>
      <div class="foot-mark"><i></i>LumaWireHub</div>
      <div class="copyright">Copyright © 2021 - LumaWire Hub, Inc.<br>All Right Reserved</div>
    </footer>
  </section>

  <!-- SINGLE PRODUCT -->
  <section class="page" style="left:491px;top:475px;height:677px">
    <div class="topbar"><div><b>&#9990; Call Us:</b> (555) 014-2287</div><div><span>Login</span><span>Register</span></div></div>
    <header class="masthead"><div class="wordmark"><i></i>LumaWireHub</div><div class="search">Enter Product name<b>SEARCH</b></div><div class="utils"><svg><use href="#i-cart"/></svg><svg><use href="#i-heart"/></svg></div></header>
    <nav class="nav"><span class="cats">CATEGORIES ▾</span><span>HOME</span><span>ABOUT US</span><span>LINE CARD</span><span>GOV/EDU BUYERS</span><span>RESELLERS</span><span>CONTACT</span></nav>
    <div class="hero" role="img" aria-label="Banner photo of a fiber optic patch panel"><h1 style="top:11px;line-height:1.2">BendRight Fiber<br>Patch Cables</h1><svg><use href="#i-hero"/></svg></div>
    <div class="body">
      <div class="crumbs">Home / BendRight Fiber Patch Cables / <b>OS2 LC LC Fiber Patch Cable | BendRight Plenum DX 9/125 Singlemode</b></div>
      <div class="prod-shot" role="img" aria-label="Blue LC duplex connectors on a white cable"></div>
      <div class="thumbs"><div role="img" aria-label="Product view 1"></div><div role="img" aria-label="Product view 2"></div><div role="img" aria-label="Product view 3"></div><div role="img" aria-label="Product view 4"></div></div>
      <div class="info">
        <h2>OS2 LC LC Fiber Patch Cable | BendRight Plenum DX 9/125 Singlemode</h2>
        <div class="stars">★★★★★ <small>(Read Reviews)</small></div>
        <div class="price">$20.95</div>
        <p>OS2 LC LC BendRight Fiber Patch Cables | Plenum Duplex Single-Mode Fiber Jumper with Lumora Glass 9/125um core/cladding. BendRight flexible boot bends and stays in any direction up to 90 degrees. Plenum OFNP, yellow, 2.0mm fiber patch cable. Reliable 1/10/40/100 Gigabit Singlemode cable that comes pre-terminated with 1.25mm SFP ceramic ferrule LC connectors.</p>
      </div>
      <div class="opts">
        <div class="qty">Quantity<div class="box"><span>-</span><span>1</span><span>+</span></div></div>
        <div>Length<div class="box len">3m ▾</div></div>
        <div class="paycard">PayCard</div>
      </div>
      <div class="share"><span>Post</span><span>Share</span><span>Save</span><span>Pin</span></div>
      <div class="buy"><div class="btn stock">IN STOCK</div><div class="btn add">ADD TO CART</div></div>
      <div class="tabs-card">
        <div class="tabs"><span class="on">DATA SHEET</span><span>MORE INFO</span><span>BULK ORDER / PART# LIST</span><span>2 REVIEWS</span></div>
        <ul class="specs">
          <li><b>Description</b>BendRight Singlemode Fiber Patch Cable | 1/10/100Gb 9/125 OS2 Flexible Boot Jumper</li>
          <li><b>Product Type</b>Plenum OFNP Fiber Optic Patch Cable</li>
          <li><b>Cable Type</b>Male to Male Pre-terminated Fiber Optic Jumpers / Fibre Network Patch Cables</li>
          <li><b>Termination</b>LC to LC Fiber Optic Cable</li>
          <li><b>Polish Type</b>UPC</li>
          <li><b>Connector 1</b>BendRight LC Duplex 1.25mm Ceramic Ferrule Connector With Flexible Boot</li>
          <li><b>Polish Connector 1</b>UPC (Ultra Physical Contact)</li>
          <li><b>Connector 2</b>BendRight LC Duplex 1.25mm Ceramic Ferrule Connector With Flexible Boot</li>
          <li><b>Polish Connector 2</b>UPC (Ultra Physical Contact)</li>
          <li><b>Max Connector Loss</b>0.50 dB</li>
          <li><b>Typical Connector Loss</b>0.30 dB</li>
          <li><b>Typical Return Loss</b>-55 dB</li>
          <li><b>Optical Mode Type</b>OS2 (9/125 Singlemode) - 9 micron core, 125 micron cladding. 10 Gigabit speed from 5-10km at 1310nm and 30-40km at 1550nm.</li>
          <li><b>Core / Cladding</b>9/125µm - Singlemode fiber optic cable has a 9 micron diameter fiber core and a 125 micron diameter cladding (1 micron is 1 one-millionth of a meter)</li>
          <li><b>Core Material</b>Lumora Glass Optical Fiber - low-loss, high bandwidth optical fiber and connectors to deliver innovative glass solutions for fiber optic cables.</li>
          <li><b>Mode Type</b>Singlemode - 9/125 Singlemode OS2 Fiber Cable is used for high speed fiber optic networking, excellent for retaining light pulse fidelity over long distances, high bandwidth.</li>
          <li><b>Strand Count</b>2 Fiber Strands</li>
          <li><b>Jacket Color</b>Yellow - This is the standard jacket color for single-mode fiber optic jumper cords / patch cables.</li>
          <li><b>Jacket Material</b>Plenum-rated (OFNP)</li>
          <li><b>Jacket OD</b>2.0mm Outer Diameter Jacket</li>
          <li><b>UL Rating</b>OFNP (Optical fiber, nonconductive, plenum) - Certified for use in plenum applications<br><b>Compliance</b>ROHS Compliant</li>
          <li><b>Length Options</b>15 Length Options 1 Meter to 30 Meter</li>
          <li><b>Quality Control</b>Fully inspected and tested in accordance with ANSI/TIA/EIA-455-171-A-2001 attenuation standards by a qualified fiber optic technician.</li>
          <li><b>Warranty Lifetime</b>All LumaWireHub products come with a lifetime warranty. If it stops working when it shouldn't, we'll replace it free.</li>
          <li><b>Current Specials</b>Free Shipping / Same Day Shipping available on fiber optic patch cable orders</li>
        </ul>
      </div>
      <div class="cleaners">
        <h3>FIBER OPTIC <em>CLEANERS:</em></h3>
        <span class="chev" style="left:13px">‹</span>
        <div class="carousel">
          <div><span role="img" aria-label="Fiber cleaner pen"></span>QuickWipe...</div>
          <div><span role="img" aria-label="Fiber cleaner box"></span>ClearTip II Fiber</div>
          <div><span role="img" aria-label="Fiber cleaner pen"></span>QuickWipe...</div>
          <div><span role="img" aria-label="Fiber cleaner box"></span>QuickWipe...</div>
        </div>
        <span class="chev" style="left:182px">›</span>
      </div>
    </div>
    <footer class="footer">
      <h3>Sign up for Our Newsletter</h3>
      <div class="news"><span>Email</span><b>SIGN UP</b></div>
      <div class="contact" style="left:20px"><div class="ring"><svg><use href="#i-phone"/></svg></div><div><strong>CALL US TODAY:</strong><span class="big">(555) 014-2287</span></div></div>
      <div class="contact" style="left:68px"><div class="ring"><svg><use href="#i-mail"/></svg></div><div><strong>EMAIL:</strong>sales@lumawirehub-example.com</div></div>
      <div class="contact" style="left:122px"><div class="ring"><svg><use href="#i-pin"/></svg></div><div><strong>LOCATION:</strong>Sales Office | Warehouse,<br>240 Relay Park Ave. Suite B, Fairvale,<br>CA 90000-0123<br>Hours: 8:00am - 5:00pm / Mon-Fri</div></div>
      <div class="socials"><i></i><i></i><i></i><i></i></div>
      <div class="foot-mark"><i></i>LumaWireHub</div>
      <div class="copyright">Copyright © 2021 - LumaWire Hub, Inc.<br>All Right Reserved</div>
    </footer>
  </section>

  <!-- BUYERS -->
  <section class="page" style="left:30px;top:579px;height:414px">
    <div class="topbar"><div><b>&#9990; Call Us:</b> (555) 014-2287</div><div><span>Login</span><span>Register</span></div></div>
    <header class="masthead"><div class="wordmark"><i></i>LumaWireHub</div><div class="search">Enter Product name<b>SEARCH</b></div><div class="utils"><svg><use href="#i-cart"/></svg><svg><use href="#i-heart"/></svg></div></header>
    <nav class="nav"><span class="cats">CATEGORIES ▾</span><span>HOME</span><span>ABOUT US</span><span>LINE CARD</span><span>GOV/EDU BUYERS</span><span>RESELLERS</span><span>CONTACT</span></nav>
    <div class="hero" role="img" aria-label="Banner photo of a fiber optic patch panel"><h1>GOV/EDU BUYERS</h1><svg><use href="#i-hero"/></svg></div>
    <div class="body">
      <h2 class="section-title" style="top:16px">GOVERNMENT / <em>MILITARY BUYERS</em></h2>
      <p class="abs copy" style="left:48px;top:28px;width:104px">Government buyers from state or federal levels, including branches of U.S. Government &amp; Military qualify for our Government Preferred Pricing (GPP).</p>
      <p class="abs copy" style="left:38px;top:39px;width:124px">To apply for GPP, simply fill out the below form and submit it to our Government sales department, who will process it for approval. You can either send an email or fax to (555) 017-3390. Once approved, you will be sent a unique code which you can use when ordering our products. The code will automatically deduct your government discount and will show your savings. There is absolutely no obligation to buy. Once you are approved and set up, you can use your pin code anytime you purchase from LumaWireHub. In addition, we will ship anywhere in the world, including APO addresses.</p>
      <p class="abs copy" style="left:0;right:0;top:63px">Buyers wanting LumaWireHub government purchasing details <a>Click Here</a></p>
      <div class="form-card" style="top:75px">
        <div class="form-grid">
          <div><h4>Subject Heading</h4><div class="field select">Choose</div><div class="field">Name</div><div class="field">Company</div><div class="field">Phone</div><div class="field">Email address</div></div>
          <div><h4>Preferred contact method</h4><div class="field select">Choose</div><div class="field msg">Message</div></div>
        </div>
        <div class="btn">SUBMIT</div>
      </div>
      <div class="brands" style="top:197px"><span>BendRight</span><span>ShieldCore</span><span>PlayMaker</span><span>SnugPort</span></div>
    </div>
    <footer class="footer">
      <h3>Sign up for Our Newsletter</h3>
      <div class="news"><span>Email</span><b>SIGN UP</b></div>
      <div class="contact" style="left:20px"><div class="ring"><svg><use href="#i-phone"/></svg></div><div><strong>CALL US TODAY:</strong><span class="big">(555) 014-2287</span></div></div>
      <div class="contact" style="left:68px"><div class="ring"><svg><use href="#i-mail"/></svg></div><div><strong>EMAIL:</strong>sales@lumawirehub-example.com</div></div>
      <div class="contact" style="left:122px"><div class="ring"><svg><use href="#i-pin"/></svg></div><div><strong>LOCATION:</strong>Sales Office | Warehouse,<br>240 Relay Park Ave. Suite B, Fairvale,<br>CA 90000-0123<br>Hours: 8:00am - 5:00pm / Mon-Fri</div></div>
      <div class="socials"><i></i><i></i><i></i><i></i></div>
      <div class="foot-mark"><i></i>LumaWireHub</div>
      <div class="copyright">Copyright © 2021 - LumaWire Hub, Inc.<br>All Right Reserved</div>
    </footer>
  </section>

  <!-- MENU DROPDOWN -->
  <section class="page" style="left:261px;top:613px;height:540px">
    <div class="topbar"><div><b>&#9990; Call Us:</b> (555) 014-2287</div><div><span>Login</span><span>Register</span></div></div>
    <header class="masthead"><div class="wordmark"><i></i>LumaWireHub</div><div class="search">Enter Product name<b>SEARCH</b></div><div class="utils"><svg><use href="#i-cart"/></svg><svg><use href="#i-heart"/></svg></div></header>
    <nav class="nav"><span class="cats">CATEGORIES ▾</span><span>HOME</span><span>ABOUT US</span><span>LINE CARD</span><span>GOV/EDU BUYERS</span><span>RESELLERS</span><span>CONTACT</span></nav>
    <div class="hero" role="img" aria-label="Banner photo of a fiber optic patch panel"><h1>CATEGORIES</h1><svg><use href="#i-hero"/></svg></div>
    <div class="body">
      <h2 class="section-title" style="top:10px;color:var(--crimson)">OUR PRODUCTS</h2>
      <div class="grid">
        <div class="card"><div class="thumb" role="img" aria-label="Patch cable connectors"></div><b>$8.95</b><p>OM2 LC LC Plenum Duplex Fiber Patch Cable...</p><div class="acts"><i class="cart"></i><i></i></div></div>
        <div class="card"><div class="thumb" role="img" aria-label="Patch cable connectors"></div><b>$8.95</b><p>OM2 LC LC Plenum Duplex Fiber Patch Cable...</p><div class="acts"><i class="cart"></i><i></i></div></div>
        <div class="card"><div class="thumb" role="img" aria-label="Patch cable connectors"></div><b>$8.95</b><p>OM2 LC LC Plenum Duplex Fiber Patch Cable...</p><div class="acts"><i class="cart"></i><i></i></div></div>
        <div class="card"><div class="thumb" role="img" aria-label="Patch cable connectors"></div><b>$8.95</b><p>OM2 LC LC Plenum Duplex Fiber Patch Cable...</p><div class="acts"><i class="cart"></i><i></i></div></div>
        <div class="card"><div class="thumb" role="img" aria-label="Patch cable connectors"></div><b>$8.95</b><p>OM2 LC LC Plenum Duplex Fiber Patch Cable...</p><div class="acts"><i class="cart"></i><i></i></div></div>
        <div class="card"><div class="thumb" role="img" aria-label="Patch cable connectors"></div><b>$8.95</b><p>OM2 LC LC Plenum Duplex Fiber Patch Cable...</p><div class="acts"><i class="cart"></i><i></i></div></div>
        <div class="card"><div class="thumb" role="img" aria-label="Patch cable connectors"></div><b>$8.95</b><p>OM2 LC LC Plenum Duplex Fiber Patch Cable...</p><div class="acts"><i class="cart"></i><i></i></div></div>
        <div class="card"><div class="thumb" role="img" aria-label="Patch cable connectors"></div><b>$8.95</b><p>OM2 LC LC Plenum Duplex Fiber Patch Cable...</p><div class="acts"><i class="cart"></i><i></i></div></div>
        <div class="card"><div class="thumb" role="img" aria-label="Patch cable connectors"></div><b>$8.95</b><p>OM2 LC LC Plenum Duplex Fiber Patch Cable...</p><div class="acts"><i class="cart"></i><i></i></div></div>
        <div class="card"><div class="thumb" role="img" aria-label="Coiled aqua patch cable"></div><b>$8.95</b><p>OM2 LC LC Plenum Duplex Fiber Patch Cable...</p><div class="acts"><i class="cart"></i><i></i></div></div>
        <div class="card"><div class="thumb" role="img" aria-label="Patch cable connectors"></div><b>$8.95</b><p>OM2 LC LC Plenum Duplex Fiber Patch Cable...</p><div class="acts"><i class="cart"></i><i></i></div></div>
        <div class="card"><div class="thumb" role="img" aria-label="Fiber cleaner box"></div><b>$8.95</b><p>OM2 LC LC Plenum Duplex Fiber Patch Cable...</p><div class="acts"><i class="cart"></i><i></i></div></div>
        <div class="card"><div class="thumb" role="img" aria-label="Patch cable connectors"></div><b>$8.95</b><p>OM2 LC LC Plenum Duplex Fiber Patch Cable...</p><div class="acts"><i class="cart"></i><i></i></div></div>
        <div class="card"><div class="thumb" role="img" aria-label="Fiber cleaner pen"></div><b>$8.95</b><p>OM2 LC LC Plenum Duplex Fiber Patch Cable...</p><div class="acts"><i class="cart"></i><i></i></div></div>
        <div class="card"><div class="thumb" role="img" aria-label="Fiber cleaner box"></div><b>$8.95</b><p>OM2 LC LC Plenum Duplex Fiber Patch Cable...</p><div class="acts"><i class="cart"></i><i></i></div></div>
        <div class="card"><div class="thumb" role="img" aria-label="Patch cable connectors"></div><b>$8.95</b><p>OM2 LC LC Plenum Duplex Fiber Patch Cable...</p><div class="acts"><i class="cart"></i><i></i></div></div>
      </div>
      <div class="brands" style="top:319px"><span>BendRight</span><span>ShieldCore</span><span>PlayMaker</span><span>SnugPort</span></div>
    </div>
    <footer class="footer">
      <h3>Sign up for Our Newsletter</h3>
      <div class="news"><span>Email</span><b>SIGN UP</b></div>
      <div class="contact" style="left:20px"><div class="ring"><svg><use href="#i-phone"/></svg></div><div><strong>CALL US TODAY:</strong><span class="big">(555) 014-2287</span></div></div>
      <div class="contact" style="left:68px"><div class="ring"><svg><use href="#i-mail"/></svg></div><div><strong>EMAIL:</strong>sales@lumawirehub-example.com</div></div>
      <div class="contact" style="left:122px"><div class="ring"><svg><use href="#i-pin"/></svg></div><div><strong>LOCATION:</strong>Sales Office | Warehouse,<br>240 Relay Park Ave. Suite B, Fairvale,<br>CA 90000-0123<br>Hours: 8:00am - 5:00pm / Mon-Fri</div></div>
      <div class="socials"><i></i><i></i><i></i><i></i></div>
      <div class="foot-mark"><i></i>LumaWireHub</div>
      <div class="copyright">Copyright © 2021 - LumaWire Hub, Inc.<br>All Right Reserved</div>
    </footer>
    <div class="overlay"></div>
    <div class="dropdown">
      <ul><li>BendRight Fiber Patch Cables</li><li>OS2 Singlemode Patch Cables</li><li>OM1 Multimode Patch Cables</li><li>OM2 Multimode Patch Cables</li><li>OM3 10G Multimode Patch Cables</li><li>OM4 100G Multimode Patch Cables</li><li>OM5 100G Multimode Patch Cables</li><li>Made In USA Fiber Cables</li></ul>
      <ul><li>LC Fiber Patch Cables</li><li>SC Fiber Patch Cables</li><li>ST Fiber Patch Cables</li><li>Armored Duplex Fiber Cables</li><li>OM4 Bend Insensitive - TAA</li><li>Indoor / Outdoor Fiber Cables</li><li>Plenum Fiber Patch Cables</li><li>Mode Conditioning Cables</li></ul>
      <ul><li>MPO/Trunk Fiber Optic Cables</li><li>Fiber Pigtails - 900 Micron</li><li>Network Transceivers</li><li>Fiber Patch Cable Packs</li><li>CAT Patch Cables</li><li>Bulk Cable</li><li>Custom Colors - Fiber</li><li>Fiber Cable Accessories</li></ul>
    </div>
  </section>
</main>
</body>
</html>
```